Eco conscious print and frame company needs a website

‘VURleaf is a new company that makes frames and fine art prints from sustainable bamboo. Our site should have an organic feel yet still have a professional clean look to it as well.
We need shopping cart and image uploading capabilities much like a pixelbarn or photomoth type of site only on a much smaller scale.
Currently we have 3 different styles available in sizes from 8"x8" all the way to 4ft by 8ft.
Target audience will be the lumograffic, picturely, zaphone market.

Target Market(s)

20-40 years old male and female. Picturely generation.

Industry/Entity Type

Shopping

Requirements
Must have
• Front end and back end capabilities with emphasis on image uploading and shopping cart functionality.

```html
<!DOCTYPE html>
<html lang="en">
<head>
<meta charset="utf-8">
<title>VURleaf Frame Company</title>
<link href="https://fonts.googleapis.com/css2?family=Oswald:wght@300;400&family=PT+Sans:wght@400;700&display=swap" rel="stylesheet">
<style>
:root{
  --topbar:#cfd5bd;
  --brown-dark:#2a1607;
  --brown-mid:#4a2a10;
  --wood-light:#e8c08a;
  --wood-mid:#d9aa6e;
  --green:#9bc33a;
  --green-dark:#7ea52a;
  --maroon:#6b1f1a;
  --nav-text:#6b6b5a;
  --panel:#f4f4f4;
  --footer:#e6e6e6;
  --footer-text:#555;
  --frame-wood:#e2a98e;
  --ink:#333;
}
*{box-sizing:border-box;margin:0;padding:0}
html,body{width:842px;height:1200px;overflow:hidden}
body{position:relative;font-family:"PT Sans",sans-serif;background:var(--footer)}
.abs{position:absolute}
.topbar{left:0;top:0;width:842px;height:70px;background:var(--topbar)}
.hero-bg{left:0;top:70px;width:842px;height:488px;background:radial-gradient(ellipse at 50% 40%,var(--brown-mid),var(--brown-dark) 80%)}
.wood-bg{left:0;top:558px;width:842px;height:498px;background:linear-gradient(90deg,var(--wood-mid),var(--wood-light) 30%,var(--wood-mid) 55%,var(--wood-light) 80%,var(--wood-mid))}
.logo{left:168px;top:30px;width:114px;height:113px;background:#fff;box-shadow:0 1px 4px rgba(0,0,0,.3);display:flex;align-items:center;justify-content:center}
.logo-name{font-family:"PT Sans",sans-serif;font-weight:400;font-size:20px;color:var(--ink)}
.nav{left:310px;top:50px;font-family:"Oswald",sans-serif;font-weight:300;font-size:10px;color:var(--nav-text)}
.nav a{color:inherit;text-decoration:none;position:absolute;white-space:nowrap}
.divider{top:104px;width:0;height:44px;border-left:1px dotted #9b8a78}
.shipping{left:482px;top:106px;font-family:"Oswald",sans-serif;color:#fff;line-height:1}
.shipping b{display:block;font-weight:400;font-size:22px}
.shipping span{font-size:10px;font-weight:300}
.offer{left:556px;top:106px;font-family:"Oswald",sans-serif;line-height:1}
.offer b{display:block;font-weight:300;font-size:20px;color:var(--green)}
.offer span{display:block;margin-top:6px;font-size:9px;color:#fff;font-weight:300}
.frame{border:14px solid var(--frame-wood);box-shadow:0 2px 6px rgba(0,0,0,.5);outline:1px solid #f3d3c2}
.photo-palms{background:linear-gradient(180deg,#8e9a86,#4e5a36 55%,#6a5a2e)}
.photo-barn{background:linear-gradient(180deg,#6d5a4a,#4a3a2c 60%,#7c6a5a)}
.intro{left:504px;top:190px;width:122px;color:#fff}
.intro h2{font-weight:400;font-size:16px;margin-bottom:3px}
.intro p{font-size:6.1px;line-height:10.3px;text-align:justify;color:#eadfd2;letter-spacing:-0.05px}
.btn-green{left:504px;top:310px;width:79px;height:16px;background:var(--green);color:#fff;font-family:"Oswald",sans-serif;font-weight:300;font-size:8px;display:flex;align-items:center;justify-content:center;box-shadow:0 1px 2px rgba(0,0,0,.4)}
.cat{top:355px;width:160px;height:71px;background:rgba(0,0,0,.35);font-family:"Oswald",sans-serif;font-weight:300;color:#fff;font-size:25px;line-height:1.1}
.cat .label{position:absolute;left:13px;top:50%;transform:translateY(-50%)}
.cat .art{position:absolute;right:14px;top:10px;width:66px;height:50px}
.card{top:446px;width:153px;height:180px;background:#fff}
.card .wood{position:absolute;left:8px;top:12px;right:0;bottom:28px;background:linear-gradient(90deg,#c9905e,#8a4a26 40%,#b06a3a)}
.card .ribbon{position:absolute;right:0;top:6px;width:118px;height:26px;background:var(--green);clip-path:polygon(14px 0,100% 0,100% 100%,14px 100%,0 50%);font-family:"Oswald",sans-serif;font-weight:300;color:#fff;font-size:13px;display:flex;align-items:center;justify-content:center;padding-left:10px}
.card .pct{position:absolute;right:10px;top:66px;font-family:"Oswald",sans-serif;font-weight:300;font-size:52px;color:#fff;line-height:1}
.card .band{position:absolute;left:0;right:0;bottom:0;height:28px;background:var(--green);font-family:"Oswald",sans-serif;font-weight:300;color:#fff;font-size:13px;padding-left:17px;display:flex;align-items:center}
.panel{left:166px;top:635px;width:506px;height:403px;background:var(--panel)}
.frames-title{left:206px;top:648px;font-family:"Oswald",sans-serif;font-weight:300;font-size:20px;color:var(--maroon)}
.tabs{left:277px;top:656px;font-size:9px;color:var(--maroon);display:flex;align-items:center}
.tab-active{background:var(--maroon);color:#fff;width:54px;height:12px;display:flex;align-items:center;justify-content:center}
.tab{position:absolute;white-space:nowrap}
.prod{width:80px}
.prod .thumb{width:78px;height:78px;border:8px solid var(--frame-wood);box-shadow:0 1px 2px rgba(0,0,0,.3)}
.prod p{font-size:5px;line-height:6.2px;color:var(--maroon);margin-top:4px;height:30px}
.prod .row{display:flex;align-items:center;gap:8px;margin-top:7px}
.buy{width:42px;height:14px;border-radius:3px;background:var(--green);color:#fff;font-size:10px;display:flex;align-items:center;justify-content:center}
.price{font-family:"Oswald",sans-serif;font-weight:300;font-size:10px;color:#222}
.more{left:330px;top:996px;width:187px;height:18px;border:1px solid #aaa;border-radius:3px;background:linear-gradient(#fff,#e6e6e6);font-size:11px;color:#333;display:flex;align-items:center;justify-content:center}
.foot-col{top:1068px;font-size:6px;color:var(--footer-text);line-height:12.4px}
.foot-col h4{font-size:6.5px;color:#333;font-weight:700}
.email{left:520px;top:1084px;width:130px;height:14px;background:#ddd;border:1px solid #d0d0d0;font-size:5px;color:#555;padding-left:10px;display:flex;align-items:center}
.go{left:656px;top:1087px;font-size:7px;color:#555}
.social{top:1144px;width:18px;height:18px;border-radius:3px}
</style>
</head>
<body>
<div class="abs topbar"></div>
<div class="abs hero-bg" role="img" aria-label="Dark brown damask wallpaper pattern"></div>
<div class="abs wood-bg" role="img" aria-label="Light wood plank texture"></div>

<div class="abs logo"><div class="logo-name">VURleaf</div></div>

<nav class="abs nav">
  <a style="left:0">Home</a>
  <a style="left:56px">About Us</a>
  <a style="left:121px">Services</a>
  <a style="left:186px">Frames</a>
  <a style="left:248px">Print Works</a>
  <a style="left:324px">Contact Us</a>
</nav>

<div class="abs divider" style="left:458px"></div>
<div class="abs shipping"><b>FREE</b><span>SHIPPING</span></div>
<div class="abs divider" style="left:540px"></div>
<div class="abs offer"><b>Limited time offer</b><span>SAVE UP TO 30% ON PHOTO FRAME</span></div>

<div class="abs frame photo-palms" style="left:208px;top:186px;width:137px;height:137px" role="img" aria-label="Framed photo of a child standing among palm trees"></div>
<div class="abs frame photo-barn" style="left:357px;top:186px;width:133px;height:137px" role="img" aria-label="Framed photo of a couple in front of a wooden barn"></div>

<div class="abs intro">
  <h2>Lorem Ipsum</h2>
  <p>Lorem Ipsum is simply dummy text of the printing and typesetting industry. Lorem Ipsum has been the industry's standard dummy text ever since the 1500s, when an unknown printer took a galley of type and scrambled it to make a type specimen book. It has survived not only five centuries, but also the leap into electronic typesetting, remaining essentially unchanged.</p>
</div>
<div class="abs btn-green">MORE GALLERIES</div>

<div class="abs cat" style="left:168px"><div class="label">Photo<br>Frames</div><div class="art" role="img" aria-label="Tilted framed colourful artwork" style="background:linear-gradient(135deg,#e8e0d0,#d98fb0 50%,#e8e0d0)"></div></div>
<div class="abs cat" style="left:340px"><div class="label">art<br>Frames</div><div class="art" role="img" aria-label="Open book illustration" style="background:linear-gradient(135deg,#d8ceb8,#8a7a5a)"></div></div>
<div class="abs cat" style="left:513px"><div class="label">Print</div><div class="art" role="img" aria-label="Colourful art print" style="background:linear-gradient(135deg,#f2e6e0,#e07aa0 50%,#7ab0d8)"></div></div>

<div class="abs card" style="left:170px"><div class="wood" role="img" aria-label="Wooden frame corner close-up"></div><div class="ribbon">SPECIAL OFERS</div><div class="pct">15%</div><div class="band">LOREM IPSUM</div></div>
<div class="abs card" style="left:346px"><div class="wood" role="img" aria-label="Bamboo frame corner with hanging hook" style="background:linear-gradient(90deg,#e6c08e,#c99a62 50%,#5a4a3a)"></div><div class="ribbon">SPECIAL OFERS</div><div class="pct">25%</div><div class="band">LOREM IPSUM</div></div>
<div class="abs card" style="left:522px"><div class="wood" role="img" aria-label="Wooden frame corner close-up"></div><div class="ribbon">SPECIAL OFERS</div><div class="pct">25%</div><div class="band">LOREM IPSUM</div></div>

<div class="abs panel"></div>
<div class="abs frames-title">FRAMES</div>
<div class="abs tabs">
  <div class="tab-active">wooden</div>
  <span class="tab" style="left:62px">|</span>
  <span class="tab" style="left:81px">Glass Frames</span>
  <span class="tab" style="left:153px">|</span>
  <span class="tab" style="left:172px">Plastic</span>
</div>

<div class="abs prod" style="left:206px;top:688px"><div class="thumb photo-barn" role="img" aria-label="Barn wedding photo in wooden frame"></div><p>Lorem Ipsum is simply dummy text of the printing and typesetting industry. Lorem Ipsum has been the industry's standard dummy text ever since the 1500s.</p><div class="row"><div class="buy">Buy</div><span class="price">$25.96</span></div></div>
<div class="abs prod" style="left:322px;top:688px"><div class="thumb photo-barn" role="img" aria-label="Barn wedding photo in wooden frame"></div><p>Lorem Ipsum is simply dummy text of the printing and typesetting industry. Lorem Ipsum has been the industry's standard dummy text ever since the 1500s.</p><div class="row"><div class="buy">Buy</div><span class="price">$25.96</span></div></div>
<div class="abs prod" style="left:434px;top:688px"><div class="thumb photo-barn" role="img" aria-label="Barn wedding photo in wooden frame"></div><p>Lorem Ipsum is simply dummy text of the printing and typesetting industry. Lorem Ipsum has been the industry's standard dummy text ever since the 1500s.</p><div class="row"><div class="buy">Buy</div><span class="price">$25.96</span></div></div>
<div class="abs prod" style="left:550px;top:688px"><div class="thumb photo-barn" role="img" aria-label="Barn wedding photo in wooden frame"></div><p>Lorem Ipsum is simply dummy text of the printing and typesetting industry. Lorem Ipsum has been the industry's standard dummy text ever since the 1500s.</p><div class="row"><div class="buy">Buy</div><span class="price">$25.96</span></div></div>

<div class="abs prod" style="left:206px;top:837px"><div class="thumb photo-palms" role="img" aria-label="Palm tree photo in wooden frame"></div><p>Lorem Ipsum is simply dummy text of the printing and typesetting industry. Lorem Ipsum has been the industry's standard dummy text ever since the 1500s.</p><div class="row"><div class="buy">Buy</div><span class="price">$25.96</span></div></div>
<div class="abs prod" style="left:322px;top:837px"><div class="thumb photo-palms" role="img" aria-label="Palm tree photo in wooden frame"></div><p>Lorem Ipsum is simply dummy text of the printing and typesetting industry. Lorem Ipsum has been the industry's standard dummy text ever since the 1500s.</p><div class="row"><div class="buy">Buy</div><span class="price">$25.96</span></div></div>
<div class="abs prod" style="left:434px;top:837px"><div class="thumb photo-palms" role="img" aria-label="Palm tree photo in wooden frame"></div><p>Lorem Ipsum is simply dummy text of the printing and typesetting industry. Lorem Ipsum has been the industry's standard dummy text ever since the 1500s.</p><div class="row"><div class="buy">Buy</div><span class="price">$25.96</span></div></div>
<div class="abs prod" style="left:550px;top:837px"><div class="thumb photo-palms" role="img" aria-label="Palm tree photo in wooden frame"></div><p>Lorem Ipsum is simply dummy text of the printing and typesetting industry. Lorem Ipsum has been the industry's standard dummy text ever since the 1500s.</p><div class="row"><div class="buy">Buy</div><span class="price">$25.96</span></div></div>

<div class="abs more">Click here for more products</div>

<div class="abs foot-col" style="left:170px"><h4>Get Help</h4>Customer Service<br>Order Status<br>Site Map<br>Contact us<br>Photo Upload Tools<br>Mobile Tools and TV</div>
<div class="abs foot-col" style="left:242px"><h4>About uS</h4>Learn More<br>Satisfaction Guarantee<br>Pricing<br>Terms<br>Privacy Policy<br>Gift Certificates</div>
<div class="abs foot-col" style="left:311px"><h4>Corporate</h4>About Us<br>Careers<br>Press Center<br>Investor Relations<br>Advertise With US</div>
<div class="abs email">Enter your E-mail ID</div>
<div class="abs go">GO</div>
<div class="abs social" style="left:587px;background:#3b5a99"></div>
<div class="abs social" style="left:608px;background:#4aa8d8"></div>
<div class="abs social" style="left:629px;background:#c0302a"></div>
<div class="abs social" style="left:650px;background:#e0702a"></div>
</body>
</html>
```